BUSINESS CARD MIRELLE CAVANOSI

I need a new business card for my personal business.
I am a Naturopath and Nutritionist working doing private consults in the health and wellness arena.
I would like to see designs that are, clean minimalist but colourful.
I like:
White (clean,fresh, minimalist)
pops of one colour ONLY.Choose a colour to run with and keep it simple.
green
light blue
mustard
Bright yellow
Charcoal
The final design should communicate professionalism but also be in touch with nature.
Key Information to include:
MIRELLE CAVANOSI
ABN 48 217 603 915
RQTLBE 327081
Tel 0487 639 142
NATUROPATH | HERBALIST | NUTRITON CONSULTANT
BHSc (Naturopathic Studies) Grad Dip (Naturopathy)
BACK OF CARD : YOUR NEXT APPOINTMENT ..................................
I already have a logo (picture attached)But I would be more than happy to NOT have this included. I am very Open to cards WITHOUT current logo/ ones that weave the colour of my logo but do not use the logo.
I have included pictures attached to give examples of the styles/colors I enjoy.
Updates
I have added a picture of a mortar and pestle - one just like this would be lovely to include in your entry.
TIA

```html
<!DOCTYPE html>
<html lang="en">
<head>
<meta charset="utf-8">
<title>Mirelle Cavanosi Naturopathy – Business Card</title>
<link href="https://fonts.googleapis.com/css2?family=Questrial&display=swap" rel="stylesheet">
<style>
  :root {
    --lime: #b1d13a;
    --lime-light: #d3e88a;
    --lime-pale: #e6f2bd;
    --charcoal: #5e5e5e;
    --grey-text: #6f6f6f;
    --white: #ffffff;
    --stage: #efefec;
  }
  * { box-sizing: border-box; margin: 0; padding: 0; }
  html, body {
    width: 1200px; height: 1000px; overflow: hidden;
    background: var(--stage);
    font-family: "Questrial", "Century Gothic", sans-serif;
  }
  .canvas { position: relative; width: 1200px; height: 1000px; }

  .card {
    position: absolute; left: 280px;
    width: 640px; height: 390px;
    border-radius: 28px; overflow: hidden;
    box-shadow: 0 6px 18px rgba(0,0,0,0.14);
  }

  /* Front */
  .card--front { top: 70px; background: var(--lime); }
  .front__foliage {
    position: absolute; left: 0; top: 60px; width: 400px; height: 330px;
    background: radial-gradient(ellipse at 45% 50%, rgba(255,255,255,0.35), rgba(255,255,255,0.08) 60%, rgba(255,255,255,0) 75%);
  }
  .front__brand {
    position: absolute; right: 48px; top: 34px; text-align: right; color: var(--white);
  }
  .front__name { font-size: 27px; letter-spacing: 1px; }
  .front__practice { font-size: 24px; letter-spacing: 9px; margin-top: 2px; margin-right: -9px; }
  .front__registry {
    position: absolute; right: 48px; top: 190px; text-align: right;
    color: var(--white); font-size: 12px; line-height: 1.45; letter-spacing: 0.5px;
  }

  /* Back */
  .card--back { top: 530px; background: var(--white); }
  .back__foliage {
    position: absolute; right: 0; top: 0; width: 230px; height: 390px;
    background: linear-gradient(100deg, rgba(177,209,58,0) 0%, var(--lime-pale) 25%, var(--lime-light) 65%, var(--lime) 100%);
  }
  .back__details { position: absolute; left: 52px; top: 92px; color: var(--grey-text); }
  .back__title { font-size: 31px; color: var(--charcoal); letter-spacing: 0.3px; }
  .back__title-accent { color: var(--lime); }
  .back__roles { font-size: 15px; margin-top: 6px; letter-spacing: 0.3px; }
  .back__quals { font-size: 15px; margin-top: 1px; letter-spacing: 0.3px; }

  .back__contact { position: absolute; left: 52px; bottom: 44px; list-style: none; }
  .contact__item {
    display: flex; align-items: center; gap: 9px;
    font-size: 25px; color: var(--charcoal); line-height: 1.25;
  }
  .contact__icon { width: 24px; height: 24px; flex: none; }
</style>
</head>
<body>
<main class="canvas">

  <section class="card card--front" aria-label="Card front">
    <div class="front__foliage" role="img" aria-label="Pale white leafy branch pressed into the green background"></div>
    <div class="front__brand">
      <div class="front__name">MIRELLE CAVANOSI</div>
      <div class="front__practice">NATUROPATHY</div>
    </div>
    <div class="front__registry">
      <div>ABN 48 217 603 915</div>
      <div>RQTLBE 327081</div>
    </div>
  </section>

  <section class="card card--back" aria-label="Card back">
    <div class="back__foliage" role="img" aria-label="Green leaf skeleton texture along the right edge"></div>
    <div class="back__details">
      <h1 class="back__title">MIRELLE CAVANOSI <span class="back__title-accent">NATUROPATH</span></h1>
      <p class="back__roles">NATUROPATH | HERBALIST | NUTRITON CONSULTANT</p>
      <p class="back__quals">BHSc (Naturopathic Studies) Grad Dip (Naturopathy)</p>
    </div>
    <ul class="back__contact">
      <li class="contact__item">
        <svg class="contact__icon" viewBox="0 0 24 24" aria-hidden="true">
          <circle cx="12" cy="12" r="12" fill="#b1d13a"/>
          <rect x="8.5" y="5.5" width="7" height="13" rx="1.2" fill="none" stroke="#fff" stroke-width="1.4"/>
          <line x1="11" y1="16.2" x2="13" y2="16.2" stroke="#fff" stroke-width="1.2"/>
        </svg>
        <span>0487 639 142</span>
      </li>
      <li class="contact__item">
        <svg class="contact__icon" viewBox="0 0 24 24" aria-hidden="true">
          <circle cx="12" cy="12" r="12" fill="#b1d13a"/>
          <rect x="6" y="8" width="12" height="8.5" fill="none" stroke="#fff" stroke-width="1.4"/>
          <polyline points="6,8 12,13 18,8" fill="none" stroke="#fff" stroke-width="1.4"/>
        </svg>
        <span>hello@cavanosihealth.com</span>
      </li>
    </ul>
  </section>

</main>
</body>
</html>
```